Meridale Hire

Meridale hire (Business Name) is a rental equipment provider for the civil and mining industry's. We have a range of equipment which is ready for any project as big or little as it maybe

Equipment list
Water carts
Excavators
skid steers
Front end loaders
Vehicles
Pressure washers
Plant trailers
Trailers
Machine attachments - 4in1 buckets for skid steers, rock breakers,

We have a solid base within port Hedland supplying some of the largest company's within the Pilbara.
We have a coemptive edge with our pricing Strategy have some unique options we can provide for company's.
We have a low cost operation with first class assets, we can do this by partnering with a local Indigenous owned and operated company KTV contracting, we assist each other with yard sharing, labour and equipment. This is a win win for both business and also establishes employment options for young Indigenous

The Broucher is to explain to anyone, what we do and what the differences are with our company. It will need to cover of equipment we can supply and why we are a good option for a company's projects.
The design is to establish a professional look for our company to grow within a large cooperate industry. The design can encompass our company colours and logo.

Industry/Entity Type

Mining

```html
<!DOCTYPE html>
<html lang="en">
<head>
<meta charset="utf-8">
<title>Meridale Hire – Vehicles Brochure Spread</title>
<link rel="stylesheet" href="https://fonts.googleapis.com/css2?family=Exo+2:wght@600&family=Noticia+Text&family=Arimo&display=swap">
<style>
  :root {
    --backdrop: #a8a8a8;
    --brand-yellow: #f8c400;
    --banner-yellow: #f2c21a;
    --banner-light: #f7d64a;
    --deep-brown: #372e2a;
    --tab-brown: #4a3b1a;
    --ink: #2a2418;
    --photo-top: #5c7f3a;
    --photo-mid: #8da36a;
    --photo-road: #8e9296;
  }
  * { box-sizing: border-box; margin: 0; padding: 0; }
  html, body { width: 1200px; height: 847px; overflow: hidden; }
  body { background: var(--backdrop); position: relative; }

  .spread {
    position: absolute; left: 80px; top: 74px;
    width: 1040px; height: 700px;
    display: flex;
    box-shadow: 0 12px 30px rgba(0,0,0,.35);
  }
  .page { position: relative; width: 520px; height: 700px; overflow: hidden; }

  /* Left page */
  .page--left { background: var(--deep-brown); }
  .hero-photo {
    position: absolute; left: 0; top: 0; width: 520px; height: 345px;
    background: linear-gradient(180deg, var(--photo-top) 0%, var(--photo-mid) 45%, var(--photo-road) 100%);
  }
  .section-banner {
    position: absolute; left: 70px; top: 300px; width: 450px; height: 62px;
    background: var(--banner-yellow);
  }
  .section-banner::before {
    content: ""; position: absolute; left: 0; top: 0; width: 100%; height: 18px;
    background: var(--banner-light);
  }
  .section-banner__title {
    position: absolute; left: 28px; top: 14px;
    font-family: "Exo 2", sans-serif; font-weight: 600;
    font-size: 27px; color: var(--ink); white-space: nowrap;
  }
  .intro {
    position: absolute; left: 34px; top: 390px; width: 460px;
    font-family: "Noticia Text", serif; font-size: 13.5px; line-height: 19px;
    color: var(--brand-yellow);
  }
  .intro p + p { margin-top: 22px; }

  /* Right page */
  .page--right { background: var(--brand-yellow); }
  .page-tab {
    position: absolute; left: 240px; top: 22px; width: 280px; height: 50px;
    background: var(--tab-brown);
  }
  .page-tab__title {
    position: absolute; left: 56px; top: 9px;
    font-family: "Exo 2", sans-serif; font-weight: 600; font-size: 25px;
    color: var(--brand-yellow);
  }
  .page-tab__flag { position: absolute; left: 240px; top: 72px; }
  .spec-column {
    position: absolute; width: 232px;
    font-family: "Arimo", sans-serif; font-size: 7.6px; line-height: 9.6px;
    color: var(--ink);
  }
  .spec-column p + p { margin-top: 9px; }
  .spec-column--fleet { left: 28px; top: 118px; }
  .spec-column--fitment { left: 268px; top: 88px; }
</style>
</head>
<body>
  <main class="spread">
    <section class="page page--left">
      <div class="hero-photo" role="img" aria-label="Photo of a car-carrier truck hauling vehicles along a tree-lined highway"></div>
      <div class="section-banner">
        <h2 class="section-banner__title">Trailers/Pressure Washers</h2>
      </div>
      <div class="intro">
        <p>Lorem ipsum dolor sit amet. Sadipscing elitr no invidunt ullamcorper. Takimata consectetuer diam. Eirmod iriure nonumy sanctus sadipscing invidunt amet dolore. Sanctus accumsan ipsum. Diam stet molestie. Id gubergren invidunt sit. Te invidunt te ut esse dolor justo. Vero laoreet amet ipsum dolor. Dolore diam labore voluptua aliquyam ut. Stet duis takimata amet et amet in. Rebum aliquyam stet est amet vulputate te. Dolor sea ea suscipit et euismod. Lorem consetetur ut dolore diam facilisi liber aliquip. Et iriure labore sed sanctus sed. Accusam vero facilisi diam.</p>
        <p>Nonumy at dolores et dolore vero assum vero. Accusam sadipscing possim sit consetetur quis. Tempor et in vel. Clita enim at sed et iriure eros eum. Zzril dolor erat. Minim vero duo diam. Ut sed amet iriure duo amet magna. Dolore amet vel</p>
      </div>
    </section>

    <section class="page page--right">
      <div class="page-tab"><h2 class="page-tab__title">Vehicles</h2></div>
      <svg class="page-tab__flag" width="30" height="20" viewBox="0 0 30 20" aria-hidden="true">
        <polygon points="0,0 30,0 30,20" fill="var(--tab-brown)"/>
      </svg>

      <div class="spec-column spec-column--fleet">
        <p>Trailmax 4x4 dual or single cab<br>Standard Specifications<br>Doors: Dual cab 4 single cab 2<br>Seats: Dual cab 5 single cab 2<br>Transmission: 5 Speed Manual OR Auto<br>Drive Type: 4WD<br>Brakes: ABS<br>GVM: 2780kgs<br>Body: Tray body or well body<br>Licence: C</p>
        <p>Availability: Through out western Australia</p>
        <p>Engine Specifications<br>3.0L 4 Cylinder<br>Fuel Type: Diesel<br>Fuel Capacity: 76L</p>
        <p>Accessories<br>CD Player, MP3 Compatible, AM/FM Radio<br>Air Conditioning<br>Driver &amp; Passenger Airbags</p>
        <p>Dual cab $68 Per day<br>Single Cab $60 Per day</p>
        <p>Then this would go on for different vehicles<br>This part can be generic for the whole fleet range at the start of the book some were</p>
        <p>Standard Mine Fitment on all equipment<br>Whip And Flag: used for visibility to oncoming traffic on site when going over a blind hill, sometimes referred to as a buggy whip. Our flags have a flexible light, ensuring less damage when driving under low barriers. We've got the flags that will survive the late night drive thru!<br>Spare tyres: two spares ensure that if you have a flat, you aren't stranded</p>
        <p>Wheel chock: ensure your parked vehicle doesn't roll away. These come in an assortment of sizes to meet the challenges of different vehicle sizes<br>Wheel nut idicators: these bright neon indicators will allow you to see when the wheel nuts are getting loose<br>Safety Triangles: used for traffic control in the case of a stopped vehicle. These are typically found under the passenger seat</p>
        <p>UHF Radio: for two way communication on site where reception is limited, with 80 channels</p>
        <p>Fire extinguisher: all vehicles come equipped with a fire extinguisher, with 3 sizes on hand at Meridale Hire to ensure the correct equipment is at hand to be able to put out vehicle fires</p>
      </div>

      <div class="spec-column spec-column--fitment">
        <p>First Aid Kit: kept in the vehicle at all times. This is for any emergency purposes<br>Bull bar: mounted to the front of the vehicle for optimum safety in the case of a collision. This reduces any personal injury in the case of an accident</p>
        <p>Tow Bar: assist in towing a trailer when you need to carry additional load</p>
        <p>Battery isolator: switch installed to isolate the starter motor. This is a standard compliance feature for all sites</p>
        <p>Hand brake alarm: this sounds when the key is taken out of the ignition and the hand brake isn't on<br>High rise indicators/mine lights: visible to Surface Mobile Equipment (Haul Packs). These are elevated brake &amp; indicator LED lights that are usually found on the rear of a car, such as a canopy</p>
        <p>Flashing beacon: enables you to attract the attention of others and alert them to your presence in low visibility areas or times of day</p>
        <p>Reverse Alarm: sounds when a vehicle is moving in reverse to alert others<br>Headlights ON feature: automatically turns headlights on when a vehicle is started, increasing visibility<br>Roll Over Protection (ROPS): internal bars on a vehicle, to increase the safety of the occupants in the event of a vehicle roll over. Meridale Hire's are padded to ensure comfort and safety when driving<br>External ROPS: external barrier to assist in protecting passengers and driver in the case of an accident<br>Falling Object Protection (FOPS): external protection on larger trucks and watercart to protect the occupants in the case of falling objects landing on the vehicle<br>Safety Hand Rails: for all flatbed trucks without drop sides and watercarts</p>
        <p>3 Point Access: three entrance and exit points on trucks to ensure safety<br>ID Decals: these call signs individually identify a vehicle<br>Reflective Tape: yellow reflective tape applied to sides and rear of vehicle to increase visibility<br>White Colour: compliant vehicles are white in colour to ensure visibility</p>
        <p>ABS: Anti-Locking Braking System prevents brakes from locking in emergency braking</p>
        <p>Airbags: all vehicles inlcude airbags for the event of a collision</p>
        <p>IVMS: some sites require the in-vehicle monitoring system. Read on to find out more about what Meridale Hire can provide</p>
      </div>
    </section>
  </main>
</body>
</html>
```